217 Marlow Lane Residences

designing a sign for apartment complex;
prefer colors gray white and yellow

Target Market(s)

residents coming home to their apartment

Font styles to use
Serif
Sans Serif

Colors
FFF300
FFF600
FEFA6F
FFFEC7
FFFEE8

Requirements
Must have
• black or gray, white and some yellow; easy to read and see

```html
<!DOCTYPE html>
<html lang="en">
<head>
<meta charset="UTF-8">
<title>217 Marlow Lane Residences — Sign</title>
<link rel="stylesheet" href="https://fonts.googleapis.com/css2?family=DM+Serif+Display&display=swap">
<style>
  :root {
    --ink: #1c1c1c;
    --panel-dark: #050505;
    --panel-gold: #c9975a;
    --accent-yellow: #ffd800;
    --face-light: #f6f6f6;
    --face-shade: #ebebeb;
  }
  * { margin: 0; padding: 0; box-sizing: border-box; }
  html, body {
    width: 1200px;
    height: 900px;
    overflow: hidden;
  }
  .sign {
    position: relative;
    width: 1200px;
    height: 900px;
    background: linear-gradient(160deg, var(--face-light) 0%, var(--face-shade) 100%);
    font-family: "DM Serif Display", Georgia, serif;
    color: var(--ink);
  }
  .pattern-panel {
    position: absolute;
    left: 0;
    top: 0;
    width: 368px;
    height: 900px;
    background:
      radial-gradient(circle at 50% 30%, rgba(201,151,90,0.35) 0%, rgba(201,151,90,0) 45%),
      radial-gradient(circle at 50% 75%, rgba(201,151,90,0.35) 0%, rgba(201,151,90,0) 45%),
      var(--panel-dark);
  }
  .accent-stripe {
    position: absolute;
    left: 368px;
    top: 0;
    width: 12px;
    height: 900px;
    background: var(--accent-yellow);
  }
  .address {
    position: absolute;
    left: 486px;
    top: 150px;
  }
  .address__number {
    display: block;
    font-size: 178px;
    line-height: 1;
    letter-spacing: 2px;
  }
  .address__name {
    display: block;
    margin-top: 8px;
    font-size: 108px;
    line-height: 114px;
    letter-spacing: 2px;
  }
  .address__rule {
    position: absolute;
    left: 488px;
    top: 726px;
    width: 308px;
    height: 5px;
    border-radius: 3px;
    background: var(--ink);
  }
</style>
</head>
<body>
  <main class="sign">
    <div class="pattern-panel" role="img" aria-label="Decorative black and gold floral lattice pattern"></div>
    <div class="accent-stripe"></div>
    <h1 class="address">
      <span class="address__number">217</span>
      <span class="address__name">Marlow<br>Lane<br>Residences</span>
    </h1>
    <div class="address__rule"></div>
  </main>
</body>
</html>
```